Brindle Advisory Business Card Design

Business card for business consulting company, using attached logo. We do financial and strategic consulting, and want a clean, professional image with a bit of fun. Our logo is a flat whale tail, which symbolizes the Orca whale, a highly collaborative, group based animal that is very successful in navigating the ocean, protecting the herd, and hunting. We like the logo that is blue and gray on white one one side, but would be open to a blue card with white lettering on the other side... or whatever you'd suggest
Updates
Hi all - I have had the logo modified to take the shadowing off the tail. I will post it on the brief... under a file name called updated logo. thank you Added Saturday, April 25, 2015
Target Market(s)
Small to medium sized businesses ($10M to $500M in revenue per year), financial and sales executives, general managers, attorneys and CPAs
Industry/Entity Type
Financial
Contact Information for Business Card
Want company name, contact info - name, title, telephone, email, website, linkedin, twitter and Facebook. No physical address yet.
Requirements
Must have
- contemporary design, bold, strong, confident but with a bit of fun. prominently feature the logo and the whale tail icon
Nice to have
- unique touches that would differentiate us from a regular card... for example, logo and writing all on front on white background, but on back - logo in white on a blue background
- open to idea of different shapes of card than standard... but not sure
Should not have
- ?

```html
<!DOCTYPE html>
<html lang="en">
<head>
<meta charset="utf-8">
<title>Brindle Advisory Business Card</title>
<link rel="stylesheet" href="https://fonts.googleapis.com/css2?family=Source+Sans+3:wght@400;600;700&display=swap">
<style>
  :root {
    --stage: #e8e5e1;
    --navy: #1f3a7a;
    --navy-deep: #1b2f63;
    --ink: #1c2f66;
    --grey: #8a8a8a;
    --paper: #ffffff;
    --tint: #e4e4e4;
  }
  * { margin: 0; padding: 0; box-sizing: border-box; }
  html, body { width: 1200px; height: 1000px; overflow: hidden; }
  body {
    background: var(--stage);
    font-family: "Source Sans 3", "Helvetica Neue", Arial, sans-serif;
    position: relative;
  }
  .card {
    position: absolute;
    top: 150px;
    width: 424px;
    height: 705px;
    border-radius: 24px;
    overflow: hidden;
  }
  .card-back { left: 145px; background: var(--navy); }
  .card-front { left: 630px; background: var(--paper); }

  .back-pattern {
    position: absolute; inset: 0;
    background: linear-gradient(180deg, #22407f 0%, var(--navy) 60%, #213d7c 100%);
  }
  .back-brand {
    position: absolute; left: 50px; top: 592px;
    display: flex; align-items: center; gap: 12px;
    color: var(--paper); font-size: 38px; font-weight: 600; letter-spacing: -0.5px;
  }
  .back-brand .mark { width: 22px; height: 22px; background: var(--paper); border-radius: 3px; }

  .front-pattern {
    position: absolute; right: 0; top: 0; width: 260px; height: 240px;
    background: radial-gradient(ellipse at 100% 0%, var(--tint) 0%, rgba(228,228,228,0.5) 45%, rgba(255,255,255,0) 75%);
  }
  .front-brand { position: absolute; left: 35px; top: 81px; }
  .front-brand .row { display: flex; align-items: center; gap: 10px; }
  .front-brand .mark { width: 53px; height: 53px; background: var(--navy-deep); border-radius: 6px; }
  .front-brand .name { color: var(--navy-deep); font-size: 38px; font-weight: 600; letter-spacing: -0.5px; }
  .front-brand .tagline {
    display: block; text-align: right; color: var(--navy-deep);
    font-size: 12px; margin-top: -10px;
  }

  .person { position: absolute; left: 35px; top: 327px; }
  .person .full-name { color: var(--ink); font-size: 20px; }
  .person .full-name strong { font-weight: 700; }
  .person .role { color: var(--grey); font-size: 17px; margin-top: -2px; }

  .address { position: absolute; left: 35px; top: 423px; color: var(--ink); font-size: 17px; line-height: 23px; }

  .contact-list, .social-list {
    position: absolute; left: 35px; list-style: none;
    color: var(--grey); font-size: 17px; line-height: 21.5px;
  }
  .contact-list { top: 486px; }
  .social-list { top: 560px; }
  .contact-list li, .social-list li { display: flex; align-items: center; gap: 6px; }
  .icon { width: 13px; height: 13px; flex: none; }
  .social-dot { width: 13px; height: 13px; background: var(--ink); border-radius: 2px; flex: none; }
</style>
</head>
<body>
  <section class="card card-back" aria-label="Card back">
    <div class="back-pattern" role="img" aria-label="Repeating pattern of the brand symbol in darker navy"></div>
    <div class="back-brand"><span class="mark"></span>Brindle Advisory</div>
  </section>

  <section class="card card-front" aria-label="Card front">
    <div class="front-pattern" role="img" aria-label="Faint repeating brand symbol pattern fading from the top right corner"></div>
    <div class="front-brand">
      <div class="row"><span class="mark"></span><span class="name">Brindle Advisory</span></div>
      <span class="tagline">business consulting</span>
    </div>

    <div class="person">
      <p class="full-name"><strong>Daniel</strong> Hartwell</p>
      <p class="role">Founder / CEO</p>
    </div>

    <p class="address">14 Calloway Street<br>Ashbury VIC 3190</p>

    <ul class="contact-list">
      <li>
        <svg class="icon" viewBox="0 0 16 16" aria-hidden="true"><path fill="#1c2f66" d="M2 6c0-2 3-3 6-3s6 1 6 3l-2 1-1-2H5L4 7 2 6zm2 2h8l1 5H3l1-5zm4 1.5a1.5 1.5 0 100 3 1.5 1.5 0 000-3z"/></svg>
        555 010 2048
      </li>
      <li>
        <svg class="icon" viewBox="0 0 16 16" aria-hidden="true"><rect x="1" y="3" width="14" height="10" fill="#1c2f66"/><path d="M1.5 3.5L8 9l6.5-5.5" stroke="#fff" stroke-width="1.2" fill="none"/></svg>
        info@brindleadvisory.com
      </li>
      <li>
        <svg class="icon" viewBox="0 0 16 16" aria-hidden="true"><g fill="none" stroke="#1c2f66" stroke-width="1.3"><circle cx="8" cy="8" r="6.5"/><ellipse cx="8" cy="8" rx="3" ry="6.5"/><path d="M1.5 8h13M2.5 4.8h11M2.5 11.2h11"/></g></svg>
        www.brindleadvisory.com
      </li>
    </ul>

    <ul class="social-list">
      <li><span class="social-dot"></span>brindleadvisory</li>
      <li><span class="social-dot"></span>@brindleadvisory</li>
      <li><span class="social-dot"></span>brindleadvisory</li>
    </ul>
  </section>
</body>
</html>
```